Dumpster rentals winter2019 print ad

Seeking an ad design for use in several local small newspapers. Size of the printed ad will vary slightly so we are looking for a rectangular ad that can be sized by the newspaper to fit their page requirements. see attached sample of an ad from last year a paper created in house. The basic info in the sample ad is what we require. Looking for something a little lighter, easier to read that will appear well in both print and black and white. Humor is OK. We have truck and dumpster photos if you need them.<br/>See our web site for more info: www.haulbinquick.com and www.haulbinquickcentral.com and www.oakbendcontainers.com.
Designer to choose colors to be used in the design.

```html
<!DOCTYPE html>
<html lang="en">
<head>
<meta charset="utf-8">
<title>Roll Off Dumpster Rental – Print Ad</title>
<link href="https://fonts.googleapis.com/css2?family=Anton&family=Oswald:wght@500;600&family=Montserrat:wght@400;800&family=Exo+2:wght@300&display=swap" rel="stylesheet">
<style>
  :root{
    --page:#f2f2f2;
    --ink:#0b0b0b;
    --paper:#fbfbfb;
    --white:#ffffff;
    --accent:#ffd400;
    --accent-deep:#f6b800;
    --edge:#5a5a5a;
  }
  html,body{margin:0;padding:0;overflow:hidden;}
  body{width:800px;height:1200px;background:var(--page);position:relative;}
  .ad-slot{position:absolute;left:130px;width:540px;height:540px;overflow:hidden;}
  .ad-slot--color{top:40px;}
  .ad-slot--mono{top:620px;}
  .ad{
    --title-top:var(--ink);
    --title-rest:var(--accent-deep);
    --column:linear-gradient(180deg,#ffe600 0%,#ffd000 55%,#fbb900 100%);
    --badge:var(--accent);
    --cta:var(--accent);
    --url-bar:var(--accent);
    --url-ink:var(--ink);
    --photo:linear-gradient(160deg,#6f8fa8 0%,#7c8a5c 50%,#9a8d74 100%);
    --truck:linear-gradient(180deg,#d9d9d9 0%,#ffffff 40%,#3a3a3a 100%);
    position:absolute;left:0;top:0;width:906px;height:906px;
    transform:scale(0.596);transform-origin:0 0;
    background:var(--paper);font-family:"Montserrat",sans-serif;color:var(--ink);
  }
  .ad--mono{
    --title-rest:#1a1a1a;
    --column:linear-gradient(180deg,#e4e4e4 0%,#d2d2d2 100%);
    --badge:linear-gradient(180deg,#e2e2e2,#bdbdbd);
    --cta:#ffffff;
    --url-bar:var(--ink);
    --url-ink:var(--white);
    --photo:linear-gradient(160deg,#a9a9a9 0%,#6c6c6c 50%,#8e8e8e 100%);
  }
  .headline{position:absolute;left:62px;top:32px;margin:0;font-family:"Anton",sans-serif;font-weight:400;font-size:88px;line-height:78px;letter-spacing:-1px;color:var(--title-rest);}
  .headline span{display:block;white-space:nowrap;}
  .headline .headline-top{color:var(--title-top);}
  .badges{position:absolute;left:63px;top:282px;height:58px;display:flex;font-family:"Oswald",sans-serif;font-weight:500;font-size:26px;line-height:58px;letter-spacing:-0.3px;}
  .badge{display:flex;align-items:center;justify-content:center;gap:7px;box-sizing:border-box;height:58px;padding:0 6px;white-space:nowrap;}
  .badge--price{background:var(--badge);color:var(--ink);width:168px;}
  .badge--delivery{background:var(--ink);color:var(--white);width:222px;}
  .badge svg{width:18px;height:18px;flex:none;}
  .truck-photo{position:absolute;left:50px;top:355px;width:465px;height:255px;background:var(--truck);border-radius:30px 60px 20px 20px;}
  .side-column{position:absolute;left:508px;top:0;width:346px;height:565px;background:var(--column);border-left:6px solid var(--edge);border-right:6px solid var(--edge);box-sizing:border-box;}
  .perks{position:absolute;left:550px;top:42px;margin:0;padding:0;list-style:none;font-family:"Exo 2",sans-serif;font-weight:300;font-size:28px;line-height:46px;}
  .perks li{display:flex;align-items:center;gap:12px;white-space:nowrap;}
  .perks svg{width:18px;height:18px;}
  .phone-box{position:absolute;left:543px;top:188px;width:279px;height:152px;box-sizing:border-box;background:var(--ink);color:var(--white);border:3px solid var(--white);border-radius:28px;text-align:center;padding-top:20px;white-space:nowrap;}
  .phone-main{font-family:"Oswald",sans-serif;font-weight:500;font-size:38px;line-height:44px;}
  .phone-alt{font-family:"Montserrat",sans-serif;font-weight:800;font-size:22px;line-height:28px;}
  .phone-alt small{font-weight:400;font-size:17px;}
  .photo-grid{position:absolute;left:533px;top:358px;width:293px;height:246px;display:grid;grid-template-columns:1fr 1fr;grid-template-rows:1fr 1fr;gap:6px;}
  .photo{background:var(--photo);}
  .message-band{position:absolute;left:50px;top:565px;width:805px;height:185px;background:var(--ink);border-radius:0 0 40px 40px;color:var(--white);text-align:center;box-sizing:border-box;padding-top:68px;white-space:nowrap;}
  .message-title{font-family:"Oswald",sans-serif;font-weight:500;font-size:25px;line-height:32px;}
  .message-sub{font-size:20px;line-height:34px;letter-spacing:1px;}
  .message-cta{font-family:"Oswald",sans-serif;font-weight:500;font-size:30px;line-height:40px;color:var(--cta);}
  .brand{position:absolute;left:62px;top:795px;display:flex;align-items:center;gap:14px;font-family:"Montserrat",sans-serif;font-weight:800;white-space:nowrap;}
  .brand-mark{width:40px;height:40px;background:var(--url-bar);}
  .brand-name{font-size:40px;line-height:44px;}
  .brand-tag{font-size:20px;line-height:24px;}
  .prices{position:absolute;left:472px;top:805px;width:373px;white-space:nowrap;}
  .prices-label{font-family:"Exo 2",sans-serif;font-weight:300;font-size:24px;text-align:center;margin-bottom:4px;}
  .prices-url{background:var(--url-bar);color:var(--url-ink);font-family:"Exo 2",sans-serif;font-size:25px;line-height:34px;padding-left:10px;}
</style>
</head>
<body>
  <svg width="0" height="0" style="position:absolute">
    <symbol id="tick" viewBox="0 0 20 20"><circle cx="10" cy="10" r="8.5" fill="none" stroke="currentColor" stroke-width="1.6"/><path d="M6 10.5l3 3 5-6" fill="none" stroke="currentColor" stroke-width="1.8"/></symbol>
  </svg>

  <div class="ad-slot ad-slot--color">
    <section class="ad">
      <h1 class="headline"><span class="headline-top">ROLL OFF</span><span>DUMPSTER</span><span>RENTAL</span></h1>
      <div class="badges">
        <div class="badge badge--price"><svg><use href="#tick"/></svg>BEST PRICE</div>
        <div class="badge badge--delivery"><svg><use href="#tick"/></svg>RAPID DELIVERY</div>
      </div>
      <div class="side-column"></div>
      <div class="truck-photo" role="img" aria-label="Roll off truck carrying a dumpster"></div>
      <ul class="perks">
        <li><svg><use href="#tick"/></svg>EASY</li>
        <li><svg><use href="#tick"/></svg>TIME-SAVING</li>
        <li><svg><use href="#tick"/></svg>AFFORDABLE</li>
      </ul>
      <div class="phone-box">
        <div class="phone-main">1-888-42-HAULS</div>
        <div class="phone-alt">(1-888-424-2857)</div>
        <div class="phone-alt"><small>or</small> 410-555-0186</div>
      </div>
      <div class="message-band">
        <div class="message-title">NEED TO DISPOSE OF JUNK, TRASH, CONSTRUCTION OR DEMOLITON QUICKLY?</div>
        <div class="message-sub">OAK BEND Roll Off &amp; Recycling has your solution</div>
        <div class="message-cta">RENT A DUMPSTER !</div>
      </div>
      <div class="photo-grid">
        <div class="photo" role="img" aria-label="Truck delivering a dumpster at a job site"></div>
        <div class="photo" role="img" aria-label="Dumpster placed on a yard with debris"></div>
        <div class="photo" role="img" aria-label="Dumpster being tilted off the truck"></div>
        <div class="photo" role="img" aria-label="Truck loading a full dumpster"></div>
      </div>
      <div class="brand">
        <div class="brand-mark"></div>
        <div><div class="brand-name">OAK BEND</div><div class="brand-tag">Roll Off &amp; Recycling</div></div>
      </div>
      <div class="prices">
        <div class="prices-label">DUMPSTER SIZES &amp; PRICES AT:</div>
        <div class="prices-url">www.HaulBinQuick.com</div>
      </div>
    </section>
  </div>

  <div class="ad-slot ad-slot--mono">
    <section class="ad ad--mono">
      <h1 class="headline"><span class="headline-top">ROLL OFF</span><span>DUMPSTER</span><span>RENTAL</span></h1>
      <div class="badges">
        <div class="badge badge--price"><svg><use href="#tick"/></svg>BEST PRICE</div>
        <div class="badge badge--delivery"><svg><use href="#tick"/></svg>RAPID DELIVERY</div>
      </div>
      <div class="side-column"></div>
      <div class="truck-photo" role="img" aria-label="Roll off truck carrying a dumpster, black and white"></div>
      <ul class="perks">
        <li><svg><use href="#tick"/></svg>EASY</li>
        <li><svg><use href="#tick"/></svg>TIME-SAVING</li>
        <li><svg><use href="#tick"/></svg>AFFORDABLE</li>
      </ul>
      <div class="phone-box">
        <div class="phone-main">1-888-42-HAULS</div>
        <div class="phone-alt">(1-888-424-2857)</div>
        <div class="phone-alt"><small>or</small> 410-555-0186</div>
      </div>
      <div class="message-band">
        <div class="message-title">NEED TO DISPOSE OF JUNK, TRASH, CONSTRUCTION OR DEMOLITON QUICKLY?</div>
        <div class="message-sub">OAK BEND Roll Off &amp; Recycling has your solution.</div>
        <div class="message-cta">RENT A DUMPSTER!</div>
      </div>
      <div class="photo-grid">
        <div class="photo" role="img" aria-label="Truck delivering a dumpster at a job site"></div>
        <div class="photo" role="img" aria-label="Dumpster placed on a yard with debris"></div>
        <div class="photo" role="img" aria-label="Dumpster being tilted off the truck"></div>
        <div class="photo" role="img" aria-label="Truck loading a full dumpster"></div>
      </div>
      <div class="brand">
        <div class="brand-mark"></div>
        <div><div class="brand-name">OAK BEND</div><div class="brand-tag">Roll Off &amp; Recycling</div></div>
      </div>
      <div class="prices">
        <div class="prices-label">DUMPSTER SIZES &amp; PRICES AT:</div>
        <div class="prices-url">www.HaulBinQuick.com</div>
      </div>
    </section>
  </div>
</body>
</html>
```